K.T cleaning services

Want to attract different crowds for industrial, initial, commercial cleaning and window and carpet cleaning to be put on as well. A nice simple design where the K.T to be the logo maybe in a shape. And our slogan, K.T time K.T place K.T clean.

Target Market(s)

Constructions companies, office buildings, apartments, house owners,

Industry/Entity Type

Industrial

Contact Information for Business Card

Manager Gordon Tesslow 0437 851062

Logo Text

K.T Cleaning Services

Logo styles of interest
Emblem Logo
Requirements
Must have
• Email: k.tcleaning@mailnest-example.com

Slogan: K.T Time K.T Place K.T Clean

Family business equals quality
Nice to have
• I would to see ( K.T) inside a badge, and cleaning services underneath. Simple but eye catching please...

```html
<!DOCTYPE html>
<html lang="en">
<head>
<meta charset="utf-8">
<title>K.T Cleaning Services – Business Card</title>
<link rel="stylesheet" href="https://fonts.googleapis.com/css2?family=Arimo:wght@400;700&display=swap">
<style>
  :root {
    --stage-light: #4b97c9;
    --stage-dark: #1b5b8c;
    --card-deep: #06118a;
    --card-mid: #1a3fc4;
    --card-glow: #7fc3f5;
    --band: #1f4fd6;
    --accent: #3fa9ff;
    --text-light: #ffffff;
    --slogan: #e6f3ff;
  }
  * { margin: 0; padding: 0; box-sizing: border-box; }
  html, body { width: 950px; height: 1200px; overflow: hidden; }
  body {
    font-family: "Arimo", Arial, sans-serif;
    background: radial-gradient(ellipse at 50% 45%, var(--stage-light) 0%, var(--stage-dark) 100%);
    position: relative;
  }
  .card {
    position: absolute;
    left: 106px;
    width: 746px;
    height: 442px;
    overflow: hidden;
    background: linear-gradient(100deg, var(--card-mid) 0%, #0d1fa8 45%, var(--card-deep) 100%);
    box-shadow: 0 6px 18px rgba(0, 20, 60, 0.45);
  }
  .card--front { top: 163px; }
  .card--back { top: 634px; }
  .card__texture {
    position: absolute;
    inset: 0;
    background: radial-gradient(ellipse 55% 110% at 0% 85%, rgba(127, 195, 245, 0.85) 0%, rgba(90, 150, 235, 0.35) 45%, rgba(20, 50, 190, 0) 80%);
  }
  .brand {
    position: absolute;
    display: flex;
    align-items: center;
    justify-content: center;
    text-align: center;
    color: var(--text-light);
    font-weight: 700;
    line-height: 1.15;
  }
  .card--front .brand { left: 514px; top: 26px; width: 194px; height: 185px; font-size: 30px; }
  .card--back .brand { left: 260px; top: 77px; width: 226px; height: 214px; font-size: 36px; }
  .name-band {
    position: absolute;
    left: 374px; top: 231px;
    width: 372px; height: 81px;
    background: var(--band);
    text-align: right;
    padding: 8px 36px 0 0;
    color: var(--text-light);
  }
  .name-band__name { font-size: 25px; line-height: 32px; }
  .name-band__surname { color: var(--accent); }
  .name-band__role { font-size: 20px; line-height: 28px; }
  .contact {
    position: absolute;
    right: 34px;
    display: flex;
    align-items: center;
    gap: 10px;
    color: var(--text-light);
    font-size: 24px;
  }
  .contact--email { top: 344px; }
  .contact--phone { top: 381px; }
  .contact svg { flex: none; }
  .slogan {
    position: absolute;
    left: 0; width: 100%;
    text-align: center;
    color: var(--slogan);
    font-size: 25px;
    line-height: 36px;
    text-shadow: 0 0 8px rgba(120, 190, 255, 0.9);
  }
  .slogan--first { top: 323px; }
  .slogan--second { top: 359px; }
</style>
</head>
<body>

<section class="card card--front">
  <div class="card__texture" role="img" aria-label="Halftone dot texture fading in from the lower left"></div>
  <div class="brand">K.T Cleaning Services</div>
  <div class="name-band">
    <p class="name-band__name">Gordon<span class="name-band__surname">Tesslow</span></p>
    <p class="name-band__role">Manager</p>
  </div>
  <p class="contact contact--email">
    <svg width="26" height="20" viewBox="0 0 26 20" aria-hidden="true">
      <rect x="1.5" y="1.5" width="23" height="17" fill="none" stroke="#fff" stroke-width="2"/>
      <path d="M1.5 1.5 L13 11 L24.5 1.5 M1.5 18.5 L10 9.5 M24.5 18.5 L16 9.5" fill="none" stroke="#fff" stroke-width="2"/>
    </svg>
    k.tcleaning@mailnest-example.com
  </p>
  <p class="contact contact--phone">
    <svg width="20" height="22" viewBox="0 0 20 22" aria-hidden="true">
      <path d="M5 1 L8 6 L6 8.5 C7 12 9.5 14.5 12.5 16 L15 13.5 L19.5 16.5 L17 20.5 C9 20 2 12 1.5 4 Z" fill="#fff"/>
    </svg>
    0437 851062
  </p>
</section>

<section class="card card--back">
  <div class="card__texture" role="img" aria-label="Halftone dot texture fading in from the lower left"></div>
  <div class="brand">K.T Cleaning Services</div>
  <p class="slogan slogan--first">K.T Time K.T Place K.T Clean</p>
  <p class="slogan slogan--second">Family business equals quality</p>
</section>

</body>
</html>
```